CV brochure for Top Management Position

I need me to introduce myself a brochure design for a CV brochure in. So sort of a resume in booklet format. The design should be serious for a convey on the other, the viewer that I stand for the new world of digitization. The brochure is intended to convey that I am a "Digital Leader". With the brochure boards, boards of directors and decision makers of enterprises should pay attention to my person. It must not be a 0815 design of the rod. The design should already be addressed with the front page of the topic Digital Leader, since the front page usually is the decisive criterion whether to continue dealing with the person or not. I am now CIO (IT manager) and wants to move with the brochure myself from this technique corner out and thus make it interesting for other positions. The positions are in absolute top management, the board, management, supervisory anchored and deal primarily with the digital transformation and the new digital world. So should appear with security on the front page a concise picture of me. but I am also very open to any alternative proposal brochure. Here you can see my current CV with picture and the basic content. The brochure is even more responsive to the social skills and not only to the technical projects implemented as before.

Target Market(s)

Top management, CxO level, supervisory boards, large companies, large Mittlestandsunternehmen

Industry/Entity Type

Management

Font styles to use
Serif
Sans Serif

Requirements
Must have
• see description
Nice to have
• see description
Should not have
• see description

```html
<!DOCTYPE html>
<html lang="de">
<head>
<meta charset="utf-8">
<title>Markus Heller – CV Broschüre</title>
<link rel="stylesheet" href="https://fonts.googleapis.com/css2?family=Montserrat:wght@300;400;500;600;700&family=Roboto+Condensed:wght@300;400;700&family=Tinos:wght@400;700&family=Cormorant+Garamond:ital,wght@1,500&display=swap">
<style>
:root{
  --ink:#262626;
  --band:#2d2d2f;
  --band-hi:#3b3b3d;
  --paper:#f3f3f3;
  --rule:#9a9a9a;
  --text:#3a3a3a;
  --muted:#7a7a7a;
  --white:#ffffff;
  --foot:#cfcfcf;
  --stage-center:#f2f2f2;
  --stage-edge:#a9a9a9;
}
*{margin:0;padding:0;box-sizing:border-box}
html,body{width:917px;height:1200px;overflow:hidden}
body{
  background:radial-gradient(ellipse at 50% 45%,var(--stage-center) 0%,#d4d4d4 55%,var(--stage-edge) 100%);
  font-family:"Roboto Condensed",Arial,sans-serif;color:var(--text);position:relative;
}
.page-label{position:absolute;width:364px;text-align:center;font-family:"Tinos","Times New Roman",serif;font-weight:700;font-size:19px;color:#111}
.page{position:absolute;width:364px;height:516px;background:var(--paper);box-shadow:0 2px 8px rgba(0,0,0,.35);overflow:hidden}
.p1{left:75px;top:66px}.p2{left:464px;top:66px}.p3{left:75px;top:615px}.p4{left:464px;top:615px}

/* headers */
.hero-band{position:absolute;left:0;top:0;width:100%;height:144px;background:linear-gradient(180deg,var(--band-hi),var(--band))}
.head-band{position:absolute;left:0;top:0;width:100%;height:80px;background:linear-gradient(180deg,var(--band-hi),var(--band))}
.mark{position:absolute;font-family:"Montserrat",sans-serif;font-weight:300;font-size:8px;letter-spacing:1px;color:#e6e6e6}
.name-line{position:absolute;font-family:"Montserrat",sans-serif;color:#f2f2f2;white-space:nowrap}
.name-line .dr{font-family:"Cormorant Garamond",serif;font-style:italic;font-weight:500;color:#cfcfcf}
.hrule{position:absolute;height:0;border-top:.6px solid #8a8a8a}
.head-contact{position:absolute;right:22px;top:54px;text-align:right;font-family:"Montserrat",sans-serif;font-weight:300;font-size:7.6px;line-height:11px;color:#e2e2e2}
.head-contact svg{vertical-align:-1px;margin-left:3px}

/* page 1 */
.sidebar{position:absolute;left:19px;top:42px;width:120px;height:430px;background:linear-gradient(180deg,#c9c9c9 0%,#a8a8a8 25%,#7d7d7d 55%,#4a4a4a 100%)}
.portrait{position:absolute;left:17px;top:14px;width:86px;height:86px;border-radius:50%;border:4px solid #fff;background:radial-gradient(circle at 50% 40%,#cfcfcf,#8a8d94 60%,#3c3f47);box-shadow:0 1px 3px rgba(0,0,0,.3)}
.role-top{position:absolute;left:0;width:120px;text-align:center;font-family:"Montserrat",sans-serif;color:#fff}
.contacts{position:absolute;left:12px;top:174px;width:104px;color:#fff;font-family:"Roboto Condensed",sans-serif}
.contacts .lbl{font-weight:700;font-size:6.2px;letter-spacing:.8px;display:flex;align-items:center;gap:5px}
.contacts .val{font-size:6.2px;letter-spacing:.5px;margin:2px 0 0 10px;color:#f0f0f0;line-height:8px}
.contacts .item{margin-bottom:14px}
.title-block{position:absolute;left:150px;top:46px;width:190px;text-align:center}
.title-block .first{font-family:"Montserrat",sans-serif;font-size:15px;color:#f0f0f0;letter-spacing:.5px}
.title-block .first .dr{font-family:"Cormorant Garamond",serif;font-style:italic;color:#cfcfcf;font-size:17px}
.title-block .last{font-family:"Montserrat",sans-serif;font-weight:700;font-size:26px;letter-spacing:1px;color:#e8e8e8;line-height:28px}
.title-block .sub{font-family:"Montserrat",sans-serif;font-weight:300;font-size:6.8px;color:#e2e2e2;line-height:9px;margin-top:8px}

.column{position:absolute}
.sec-bar{background:var(--band);color:#fff;font-family:"Montserrat",sans-serif;font-weight:500;font-size:6.4px;letter-spacing:.8px;padding:2px 0 2px 8px;height:11px;margin-bottom:4px}
.tag{display:inline-block;background:var(--band);color:#fff;font-family:"Montserrat",sans-serif;font-weight:500;font-size:5.4px;padding:1.5px 14px 1.5px 6px;clip-path:polygon(0 0,100% 0,92% 100%,0 100%);margin:4px 0 4px}
.tl{position:relative;list-style:none;padding-left:9px}
.tl::before{content:"";position:absolute;left:2.6px;top:2px;bottom:2px;border-left:.6px solid var(--rule)}
.tl li{position:relative;font-size:4px;line-height:5px;margin-bottom:4.6px;color:#333}
.tl li::before{content:"";position:absolute;left:-8.4px;top:1px;width:3px;height:3px;border:.6px solid #555;border-radius:50%;background:var(--paper)}
.tl b{font-weight:700}
.entry{font-size:4px;line-height:5.2px;margin:1px 0 4px 9px;color:#333}
.entry b{font-weight:700}
.plain{font-size:4px;line-height:5px;color:#333;margin:0 0 5px 8px}

.ghost{position:absolute;background:radial-gradient(ellipse at 50% 45%,rgba(150,150,150,.35),rgba(200,200,200,.15) 60%,rgba(243,243,243,0) 80%)}

/* footer */
.footer{position:absolute;left:0;top:497px;width:100%;height:11px;background:var(--foot)}
.footer::after{content:"";position:absolute;right:0;top:0;width:44px;height:11px;background:var(--band);clip-path:polygon(14% 0,100% 0,100% 100%,0 100%)}
.footer .num{position:absolute;left:0;width:100%;text-align:center;top:0;font-family:"Tinos",serif;font-size:8.5px;line-height:11px;color:#111}
.footer .fmark{position:absolute;right:8px;top:0;z-index:1;font-family:"Montserrat",sans-serif;font-weight:300;font-size:5.6px;line-height:11px;color:#fff}
.footer-edge{position:absolute;left:0;top:508px;width:100%;height:8px;background:#fff}

.signoff{position:absolute;left:42px;top:450px;font-family:"Roboto Condensed",sans-serif;font-weight:300;font-size:27px;color:#c4c4c4}
</style>
</head>
<body>

<div class="page-label" style="left:75px;top:32px">Page 1</div>
<div class="page-label" style="left:464px;top:32px">Page 2</div>
<div class="page-label" style="left:75px;top:1148px">Page 3</div>
<div class="page-label" style="left:464px;top:1148px">Page 4</div>

<!-- PAGE 1 -->
<section class="page p1">
  <div class="hero-band"></div>
  <div class="mark" style="left:232px;top:24px">Heller</div>
  <div class="hrule" style="left:168px;top:38px;width:172px"></div>
  <div class="title-block">
    <div class="first"><span class="dr">Dr.</span> MARKUS</div>
    <div class="last">HELLER</div>
    <div class="sub">Chief Information Officer (CIO)<br>Ph.D. Wirtschaftsinformatik</div>
  </div>

  <aside class="sidebar">
    <div class="portrait" role="img" aria-label="Porträtfoto von Dr. Markus Heller"></div>
    <div class="role-top" style="top:116px;font-size:8px;letter-spacing:1.4px">CHIEF DIGITAL</div>
    <div class="role-top" style="top:125px;font-size:14px;letter-spacing:1.6px">OFFICER</div>
    <div class="role-top" style="top:146px;font-size:6.6px;letter-spacing:1.4px;font-weight:300">DIGITAL LEADER</div>
    <div class="contacts">
      <div class="item"><div class="lbl"><svg width="6" height="6" viewBox="0 0 10 10"><circle cx="5" cy="5" r="4.5" fill="#fff"/><path d="M3 3l4 4M7 3l-4 4" stroke="#777" stroke-width="1.3"/></svg>CONTACTS</div></div>
      <div class="item"><div class="lbl"><svg width="6" height="7" viewBox="0 0 10 12"><path d="M5 0a4 4 0 0 1 4 4c0 3-4 8-4 8S1 7 1 4a4 4 0 0 1 4-4z" fill="#fff"/><circle cx="5" cy="4" r="1.5" fill="#777"/></svg>ADRESSE</div><div class="val">Lindenweg 4 20095 Hamburg</div></div>
      <div class="item"><div class="lbl"><svg width="6" height="6" viewBox="0 0 10 10"><rect x="0.5" y="1.5" width="9" height="8" fill="none" stroke="#fff"/><path d="M0.5 4h9" stroke="#fff"/></svg>GEBURTSDATEN</div><div class="val">14. Mai 1978 in Kassel</div></div>
      <div class="item"><div class="lbl"><svg width="6" height="6" viewBox="0 0 10 10"><rect x="1" y="3" width="8" height="7" fill="#fff"/><rect x="3" y="0" width="4" height="3" fill="#fff"/></svg>FAMILIENSTAND</div><div class="val">verheiratet | 2 Kinder</div></div>
      <div class="item"><div class="lbl"><svg width="5" height="7" viewBox="0 0 8 12"><rect x="0.5" y="0.5" width="7" height="11" rx="1" fill="none" stroke="#fff"/><circle cx="4" cy="9.5" r=".8" fill="#fff"/></svg>MOBIL</div><div class="val">+49 (0) 151 2048 3390</div></div>
      <div class="item"><div class="lbl"><svg width="7" height="5" viewBox="0 0 12 8"><rect x="0.5" y="0.5" width="11" height="7" fill="#fff"/><path d="M0.5 0.5l5.5 4 5.5-4" fill="none" stroke="#777"/></svg>E-MAIL</div><div class="val">kontakt@heller-mail.de</div></div>
      <div class="item"><div class="lbl"><svg width="6" height="6" viewBox="0 0 10 10"><circle cx="5" cy="3" r="2.5" fill="#fff"/><path d="M0.5 10a4.5 4 0 0 1 9 0z" fill="#fff"/></svg>PROFIL</div><div class="val">www.netzprofil.de/heller</div></div>
    </div>
  </aside>

  <div class="column" style="left:147px;top:152px;width:196px">
    <div class="sec-bar">AUF EINEN BLICK</div>
    <ul class="tl">
      <li><b>Kommunikationsstarke Führungspersönlichkeit</b> mit mehrjähriger Erfahrung in Leitungsfunktionen im IT-Bereich, aktuell <b>Chief Information Officer (CIO) und Chief Digital Officer (CDO)</b></li>
      <li>Umfangreiche <b>Fachexpertise</b> in Konzeption und <b>Weiterentwicklung von IT-Unternehmensstrategien</b> | Effizienzsteigerung im IT-Bereich | <b>Optimierung der IT-Service-Strukturen</b> | Planung und Durchführung <b>konzernweiter IT-Programme</b></li>
      <li>Experte auf dem Gebiet der <b>Transformation von Unternehmen in die digitale Welt</b> (Industrie 4.0) | <b>Etablierung der IT als Business Enabler</b></li>
      <li>Führung von <b>75 MA + ca. 20 (weltweit und extern)</b>, davon 4 Führungskräfte | Budget i.H.v. <b>22 Mio. €</b> p.a.</li>
      <li><b>Wissensmanagement interkultureller Kompetenz</b>, breites Technologieverständnis sowie ausgeprägter Durchsetzungs- und Teamfähigkeit</li>
      <li><b>umsetzungsstark</b> | lösungsorientiert | <b>unternehmerisch</b> | visionär</li>
    </ul>
    <div class="sec-bar" style="margin-top:6px">BERUFLICHE ERFAHRUNGEN</div>
    <span class="tag">10/2012–heute</span>
    <div class="entry"><b>Vandor Gruppe</b> | Kernstadt | www.vandor-gruppe.de<br>Weltweiter Hersteller von Präzisionswerkzeugen | 7.000 MA weltweit in ca. 50 Ländern | 900 Mio. € Umsatz<br><b style="line-height:9px">Chief Information Officer/ Chief Digital Officer</b></div>
    <ul class="tl">
      <li>Verantwortung der operativen sowie strategischen IT weltweit</li>
      <li>Verantwortung der digitalen Transformation der Firma weltweit, Umsetzung der Vision 2020</li>
      <li>Aufbau einer IT-Strategie in Abstimmung mit Geschäftsführung und Eigentümer</li>
      <li>Entwicklung und Umsetzung einer ERP-Roadmap 2020, inkl. Einführung der ERP-Suite in ca. 40 Tochtergesellschaften weltweit</li>
      <li>Aufbau eines IT-Risikomanagementsystems im Zusammenhang mit IT-GRC-Strukturen</li>
      <li>Definition einer zentralen e-Business Multichannel Architektur</li>
      <li>Aufbau einer IT-Leistungsrechnung sowie eines IT-Controllings</li>
      <li>Aufbau zweier IT Hubs in Asien und Amerika</li>
      <li>Neuausrichtung der gesamten IT-Infrastruktur (Migration der Verzeichnisdienste)</li>
      <li>Etablierung einer IT-Projektmethodik</li>
      <li>Erarbeitung eines ECM-Konzepts „Just-in-time Informationslogistik"</li>
      <li>Definition/Rollout einer Prozessmodellierungssystematik unter BPMN 2.0 und Prozessmodellierer</li>
      <li>Aufteilung der IT in Projektgeschäft und Katalog bzw. Standardgeschäft (vom Einkauf über Anforderungen bis zum Betrieb)</li>
      <li>Definition einer neuen IT-Organisation nach dem Plan-Build-Run-Prinzip</li>
    </ul>
  </div>

  <div class="footer"><span class="num">1</span><span class="fmark">Heller</span></div>
  <div class="footer-edge"></div>
</section>

<!-- PAGE 2 -->
<section class="page p2">
  <div class="head-band"></div>
  <div class="mark" style="left:118px;top:16px">Heller</div>
  <div class="name-line" style="left:22px;top:40px;font-size:15px"><span class="dr" style="font-size:17px">Dr.</span> MARKUS <b style="font-weight:700">HELLER</b></div>
  <div class="hrule" style="left:20px;top:63px;width:206px"></div>
  <div class="head-contact">+49 (0) 151 2048 3390 <svg width="5" height="7" viewBox="0 0 8 12"><rect x=".5" y=".5" width="7" height="11" rx="1" fill="none" stroke="#ddd"/></svg><br>kontakt@heller-mail.de <svg width="6" height="4" viewBox="0 0 12 8"><rect width="12" height="8" fill="#ddd"/></svg></div>

  <div class="ghost" style="left:200px;top:170px;width:164px;height:240px" role="img" aria-label="Dezentes, verblasstes Porträtfoto von Dr. Markus Heller als Hintergrund"></div>

  <div class="column" style="left:22px;top:93px;width:322px">
    <ul class="tl">
      <li>Entwicklung einer Roadmap Industrie 4.0, Erprobung diverser Industrie 4.0 Themen mit der Produktion, Erarbeitung einer IT-Security-Strategie für alle Produktionswerke, Testen von neuen „Wearables" zum Einsatz in der Produktion, Vollautomatisierung von Produktionswerken durch IT</li>
      <li>Aufbau einer neuen digitalen Einheit zur Erarbeitung von neuen Geschäftsmodellen</li>
      <li><b>Verantwortung:</b> Führung von 75 MA + ca. 20 (weltweite und externe), davon 4 Führungskräfte | Budget i.H.v. 22 Mio. €</li>
      <li><b>Erfolge:</b><br>Einführung einer globalen ERP-Strategie, Einsparung von 1/3 der Kosten bei jedem Rollout durch Einsatz der Mittelstandslösung, Verkürzung der Einführungszeiten von 1 Jahr auf 4 Monate sowie Erhöhung der Userzufriedenheit durch größere Usability und Simplicity der ERP-Anwendung<br>Erstellung und Umsetzung einer globalen IT-Strategie und komplette Neustrukturierung der IT zu einer schnelleren und agileren Arbeitsweise (Etablierung einer Two Speed IT)</li>
      <li>Erstellung einer digitalen Vision 2020</li>
      <li>Erzielung erster Online-Umsätze mit dem neuen eBusiness Konzept</li>
    </ul>
    <span class="tag">02/2010 – 09/2012</span>
    <div class="entry"><b>Kessler Gruppe</b> | Talhausen | www.kessler-fassaden.de<br>Weltweites Fassadenbauunternehmen | 1.000 Mitarbeiter | 14 Standorte weltweit<br><b style="line-height:9px">Chief Information Officer</b></div>
    <ul class="tl">
      <li>Weltweite operative und strategische IT-Verantwortung</li>
      <li>Aufbau einer IT-Strategie in Abstimmung mit den beiden Gesellschaftern</li>
      <li>Integration verschiedener Standorte in die Gruppen-IT (Austria, Shanghai, Pilsen)</li>
      <li>Projektverantwortlicher für die weltweite Einführung des ERP-Systems</li>
      <li>Definition von Anpassungsprogrammierungen und Erstellung von Konzepten für die eigenen ERP-Entwickler</li>
      <li>Entwicklung neuer Hardwarestrategien, u.a. Einführung von MFD-Geräten</li>
      <li>Aufbau eines Notfall- und Hochverfügbarkeitskonzepts für die gruppenweite IT</li>
      <li>Entwicklung einer gruppenweiten IT-Policy und IT-Umweltstrategie</li>
      <li>Aufbau von Servicestrukturen nach IT-Servicemanagement-Standards und Einführung eines Ticketingsystems<br><b>Verantwortung:</b> Führung von 10 MA, davon 1 Führungskraft | Budget i.H.v. 4 Mio. €</li>
      <li><b>Erfolge:</b><br>Neuausrichtung der IT, Erstellung einer globalen IT-Strategie</li>
      <li>Einführung eines neuen ERP-Systems</li>
      <li>Senkung der Printkosten innerhalb der gesamten Gruppe um ca. 50 % durch die Einführung einer globalen Printmanagementlösung</li>
      <li>Erhöhung der Anwenderzufriedenheit von Schulnote 3 auf 2+</li>
    </ul>
    <span class="tag">04/2008 – 01/2010</span>
    <div class="entry"><b>Nordtherm Bus Europe</b> | Bergfeld |<br>(heute Nordtherm Climate Control Systems GmbH &amp; Co. KG)<br>Klimaanlagen für Omnibusse und Sonderfahrzeuge | 200 MA<br>IT-Leiter EMEA</div>
    <ul class="tl">
      <li>IT-Verantwortung für alle EMEA-Standorte</li>
      <li>Entwicklung einer neuen IT-Strategie in Abstimmung mit der Corporate IT des Gesamtkonzerns</li>
      <li>Umsetzung der Corporate IT-Richtlinien, u.a. SOX</li>
      <li>Mitglied im globalen Projektteam „Einführung ERP"</li>
      <li>Umsetzung eines Prozessberatungsprojekts innerhalb des Unternehmens</li>
      <li>Projekt zur Erhöhung des Nutzungsgrades der ERP-Anwendung</li>
      <li>Releasewechsel des 10 Jahre alten ERP-Systems</li>
    </ul>
  </div>

  <div class="footer"><span class="num">2</span><span class="fmark">Heller</span></div>
  <div class="footer-edge"></div>
</section>

<!-- PAGE 3 -->
<section class="page p3">
  <div class="head-band"></div>
  <div class="mark" style="left:118px;top:16px">Heller</div>
  <div class="name-line" style="left:22px;top:40px;font-size:15px"><span class="dr" style="font-size:17px">Dr.</span> MARKUS <b style="font-weight:700">HELLER</b></div>
  <div class="hrule" style="left:20px;top:63px;width:206px"></div>
  <div class="head-contact">+49 (0) 151 2048 3390 <svg width="5" height="7" viewBox="0 0 8 12"><rect x=".5" y=".5" width="7" height="11" rx="1" fill="none" stroke="#ddd"/></svg><br>kontakt@heller-mail.de <svg width="6" height="4" viewBox="0 0 12 8"><rect width="12" height="8" fill="#ddd"/></svg></div>

  <div class="ghost" style="left:200px;top:250px;width:164px;height:240px" role="img" aria-label="Dezentes, verblasstes Porträtfoto von Dr. Markus Heller als Hintergrund"></div>

  <div class="column" style="left:22px;top:94px;width:322px">
    <ul class="tl">
      <li>Einführung einer Open-Source-Reporting-Lösung</li>
      <li>Mitglied des sechsköpfigen Managementboards</li>
      <li>Planung und Konzeption von Change Requests für das ERP-System<br><b>Verantwortung:</b> Führung von 4 MA | Budget i.H.v. 2 Mio. €<br><b>Erfolge:</b><br>Prozessoptimierungen und Einsparungen in allen Unternehmensbereichen sowie Upgrade des bestehenden ERP Systems</li>
      <li>Erhöhung der Anwenderzufriedenheit von Schulnote 4 auf 1,5</li>
      <li>Senkung der IT-Kosten um 20%</li>
    </ul>
    <span class="tag">07/2006 – 03/2008</span>
    <div class="entry"><b>Brendel Software GmbH</b> | Donaufeld | Projektleiter, Business Consultant Brendel Suite</div>
    <span class="tag">03/2005 – 06/2006</span>
    <div class="entry"><b>Talwerk GmbH</b> | Auenfeld | Key Account Manager</div>
    <span class="tag">03/2004 – 02/2005</span>
    <div class="entry"><b>Orvis Enterprise Solutions GmbH</b> | Waldhofen | Junior Account Manager</div>

    <div class="sec-bar" style="margin-top:6px">AUSBILDUNG</div>
    <span class="tag">09/2010 – 08/2014</span>
    <div class="entry"><b>Ph.D. in Business Management</b> | Donau Business University<br>Dissertation: <i>"Effective deployment of ERP in small and medium-size companies to get a decisive competitive edge"</i></div>
    <span class="tag">04/2006 – 10/2008</span>
    <div class="entry"><b>Master of Business Consulting (MBC)</b> | Fernhochschule Nordstadt, Standort Rheinfeld<br>Schwerpunkte: strategische Unternehmensberatung, KMU Controlling, Personalberatung und Coaching, Prozess- und Organisationsberatung, Corporate Finance-Beratung<br>Thesis: <i>"Compliance rules and the conversion in the IT sector of a middle-class enterprise with corporate affiliation"</i> Note: 2,2</div>
    <span class="tag">10/2000 – 06/2003</span>
    <div class="entry"><b>Diplom-Wirtschaftsinformatiker (DH)</b> | Duale Hochschule Südwest,<br>Berufsakademie Waldhofen und Brendel Aktiengesellschaft in Haldingen<br>Schwerpunkte: E-Business und Consulting<br>Diplomarbeit: <i>"Bedarfsanalyse betriebswirtschaftlicher Funktionalitäten als Basis für den Produktplanungsprozess"</i> Note: 1,5</div>
    <span class="tag">07/2000 – 07/1999</span>
    <div class="entry"><b>Zivildienst | Berufsförderungszentrum Auental</b></div>
    <span class="tag">07/1999</span>
    <div class="entry"><b>Allgemeine Hochschulreife | Technisches Gymnasium Lindau-Süd</b></div>
  </div>

  <div class="footer"><span class="num">3</span><span class="fmark">Heller</span></div>
  <div class="footer-edge"></div>
</section>

<!-- PAGE 4 -->
<section class="page p4">
  <div class="head-band"></div>
  <div class="mark" style="left:118px;top:16px">Heller</div>
  <div class="name-line" style="left:22px;top:40px;font-size:15px"><span class="dr" style="font-size:17px">Dr.</span> MARKUS <b style="font-weight:700">HELLER</b></div>
  <div class="hrule" style="left:20px;top:63px;width:206px"></div>
  <div class="head-contact">+49 (0) 151 2048 3390 <svg width="5" height="7" viewBox="0 0 8 12"><rect x=".5" y=".5" width="7" height="11" rx="1" fill="none" stroke="#ddd"/></svg><br>kontakt@heller-mail.de <svg width="6" height="4" viewBox="0 0 12 8"><rect width="12" height="8" fill="#ddd"/></svg></div>

  <div class="column" style="left:26px;top:93px;width:318px">
    <div class="sec-bar">FORT- UND WEITERBILDUNGEN</div>
    <span class="tag">Führung/Management</span>
    <p class="plain" style="margin-top:4px">Teilnahme an Veranstaltungen und Workshops zu Führung und Management, wie z.B.:</p>
    <p class="plain" style="margin-top:8px">Management- und Personalführungsseminar | Kessler Gruppe | 2011</p>
    <p class="plain" style="margin-top:8px">Management- und Personalführungsseminar | Nordtherm | 2008</p>
    <p class="plain" style="margin-top:8px">Feedbackgespräche, Coaching von Mitarbeitern</p>
    <p class="plain" style="margin-top:8px">Persönlichkeitsmodell zur Einschätzung von Mitarbeitern</p>

    <div class="sec-bar" style="margin-top:16px">AUSZEICHNUNGEN</div>
    <span class="tag">Digital Executive Award 2015</span>
    <p class="plain">Platzierung unter den Top 20 IT-Führungskräften im Bereich Großunternehmen und Konzerne</p>

    <div class="sec-bar" style="margin-top:16px">ZUSATZQUALIFIKATIONEN</div>
    <span class="tag">EDV-Kenntnisse</span>
    <p class="plain" style="margin-bottom:2px"><b>Anwendungsbezogen:</b> Office-Suite | Projektplanung | Prozessmodellierer | Projektportal</p>
    <p class="plain" style="margin-bottom:2px"><b>Fachbezogen:</b> ERP-Suite Kern/Analytics | Brendel Suite/industry | CRM-Plattform | Auftragssystem</p>
    <p class="plain"><b>Programmiersprachen:</b> Java | .Net | C# | SQL | PL/SQL</p>
    <span class="tag">Sprachkenntnisse</span>
    <p class="plain"><b>Deutsch:</b> Muttersprache | <b>Englisch:</b> verhandlungssicher</p>

    <div class="sec-bar" style="margin-top:20px">WEITERE ANGABEN</div>
    <span class="tag">Ausland</span>
    <p class="plain"><b>Auslandspraktikum bei Brendel Infotech Ltd. in Ahmedabad (Indien)</b></p>
    <span class="tag">Interessen</span>
    <p class="plain"><b>Sport: Fußball sowie jeglicher Ballsport, Fitness | Kochen | Reisen</b></p>
  </div>

  <div class="signoff">Hamburg, 8. März 2017</div>

  <div class="footer"><span class="num">4</span><span class="fmark">Heller</span></div>
  <div class="footer-edge"></div>
</section>

</body>
</html>
```